Business Card Design

Professional solutions in (servers, security, networks, programming)

Industry/Entity Type

Business

Contact Information for Business Card

Tarek Hounayni
Internet services and network solutions
DPV - RTLK - RTLB
netcare@qo-lam.com / 05917406238
www.qo-lam.com

```html
<!DOCTYPE html>
<html lang="en">
<head>
<meta charset="utf-8">
<title>Tarek Hounayni — Business Card</title>
<link rel="stylesheet" href="https://fonts.googleapis.com/css2?family=Tinos:wght@700&family=Jura:wght@700&family=Arimo&display=swap">
<style>
  :root {
    --page: #d9d4cf;
    --frame: #0c0c0c;
    --steel-light: #b9b9b7;
    --steel-mid: #9a9a98;
    --steel-dark: #6f6f6d;
    --ink: #111111;
    --highlight: rgba(255,255,255,0.55);
    --badge: rgba(30,30,30,0.78);
  }
  html, body {
    margin: 0;
    width: 1200px;
    height: 998px;
    overflow: hidden;
    background: var(--page);
  }
  .business-card {
    position: absolute;
    left: 60px;
    top: 178px;
    width: 1080px;
    height: 642px;
    box-sizing: border-box;
    border: 12px solid var(--frame);
    background:
      radial-gradient(ellipse at 55% 35%, var(--steel-light) 0%, var(--steel-mid) 55%, var(--steel-dark) 100%);
    box-shadow: 0 10px 30px rgba(0,0,0,0.35);
    color: var(--ink);
  }
  .tagline {
    position: absolute;
    left: 0; right: 0;
    top: 70px;
    margin: 0;
    text-align: center;
    font-family: "Tinos", serif;
    font-weight: 700;
    font-size: 56px;
    letter-spacing: 0.5px;
    text-shadow: 0 1px 0 var(--highlight);
  }
  .divider {
    position: absolute;
    left: 52px; right: 52px;
    top: 188px;
    height: 3px;
    background: var(--ink);
    box-shadow: 0 1px 0 var(--highlight);
  }
  .person-name {
    position: absolute;
    left: 0; right: 0;
    top: 232px;
    margin: 0;
    text-align: center;
    font-family: "Jura", sans-serif;
    font-weight: 700;
    font-size: 48px;
    text-shadow: 0 1px 0 var(--highlight);
  }
  .contact {
    font-family: "Arimo", sans-serif;
    text-shadow: 0 1px 0 var(--highlight);
  }
  .phone {
    position: absolute;
    left: 0; right: 0;
    top: 345px;
    text-align: center;
    font-size: 33px;
  }
  .web-line {
    position: absolute;
    left: 0; right: 0;
    top: 394px;
    display: flex;
    justify-content: center;
    align-items: center;
    gap: 14px;
    font-size: 33px;
  }
  .web-line svg { display: block; }
  .web-line .email { margin-left: 6px; }
  .badge {
    position: absolute;
    display: block;
  }
  .badge-left { left: 98px; top: 482px; }
  .badge-centre { left: 448px; top: 490px; }
  .badge-right { left: 740px; top: 482px; }
</style>
</head>
<body>
  <section class="business-card">
    <h1 class="tagline">Internet services and network solutions</h1>
    <div class="divider"></div>
    <h2 class="person-name">Tarek Hounayni</h2>
    <div class="contact phone">05917406238</div>
    <div class="contact web-line">
      <span class="website">www.qo-lam.com</span>
      <svg width="22" height="22" viewBox="0 0 22 22" aria-hidden="true">
        <rect x="1" y="1" width="20" height="20" rx="2" fill="#111"/>
        <circle cx="11" cy="11" r="6.5" fill="none" stroke="#ddd" stroke-width="1.6"/>
        <line x1="4.5" y1="11" x2="17.5" y2="11" stroke="#ddd" stroke-width="1.4"/>
        <ellipse cx="11" cy="11" rx="3" ry="6.5" fill="none" stroke="#ddd" stroke-width="1.4"/>
      </svg>
      <svg width="26" height="22" viewBox="0 0 26 22" aria-hidden="true" style="margin-left:40px">
        <rect x="1" y="1" width="24" height="20" rx="2" fill="#111"/>
        <rect x="5" y="6" width="16" height="10" fill="none" stroke="#ddd" stroke-width="1.5"/>
        <polyline points="5,6 13,12 21,6" fill="none" stroke="#ddd" stroke-width="1.5"/>
      </svg>
      <span class="email">netcare@qo-lam.com</span>
    </div>

    <svg class="badge badge-left" width="232" height="120" viewBox="0 0 232 120" role="img" aria-label="RTLK certification badge">
      <rect x="0" y="0" width="232" height="120" rx="8" fill="var(--badge)"/>
    </svg>

    <svg class="badge badge-centre" width="180" height="120" viewBox="0 0 180 120" role="img" aria-label="DPV certification badge">
      <rect x="0" y="0" width="180" height="120" rx="8" fill="var(--badge)"/>
    </svg>

    <svg class="badge badge-right" width="232" height="120" viewBox="0 0 232 120" role="img" aria-label="RTLB certification badge">
      <rect x="0" y="0" width="232" height="120" rx="8" fill="var(--badge)"/>
    </svg>
  </section>
</body>
</html>
```